Business Card Design

We need a business card design for a Non-Profit Christian Based Organization located in Milford, Pa.
Alder Ridge Helping Harbor
Is a Christ-centered organization dedicated to providing compassion and hope to homeless or near homeless, families and individuals, by meeting their basic and urgent need of food, clothing and shelter.
Updates
the logo is black and white
and must add the color green some where 00400
Industry/Entity Type
Clothing
Contact Information for Business Card
Alder Ridge Helping Harbor
P.O. Box 287
Milord, Pa 18337
Phone: (570) 413-CARE(2273)
Toll Free: (855) 413-CARE
email:Info@alderridgehh.org
email:Careline@alderridgehh.org
Our organization already has a logo.
Front of card:
Is a Christ-centered organization dedicated to providing compassion and hope to homeless or near homes, families and individual by meeting their basic and urgent need of food, clothing and shelter.(this is our Mission Statement)
On back of card:
'I was hungry and you gave me something to eat;
"I was thirsty and you gave me something to drink;
"I was a stranger and you invited me in."
Matthew 25:35
Color: Logo is black and white
Background color I would like a bright light green 00ff00(close to that)
I attached a sample of what I created on Quill Press but, I don't like the color green, nor the design (but I just wanted to give you and Idea of the Logo and Alder Ridge (one line) Helping Harbor (second line) in a different font thank you
Delia Rostova
Pr/Board of Directors

```html
<!DOCTYPE html>
<html lang="en">
<head>
<meta charset="utf-8">
<title>Alder Ridge Helping Harbor – Business Card</title>
<link rel="stylesheet" href="https://fonts.googleapis.com/css2?family=Alegreya:ital,wght@1,400&display=swap">
<style>
  :root {
    --leaf-green: #76b52a;
    --curve-shadow: #000000;
    --card-white: #ffffff;
    --ink: #111111;
    --page-bg: #ffffff;
  }
  html, body {
    margin: 0;
    padding: 0;
    width: 1200px;
    height: 761px;
    overflow: hidden;
    background: var(--page-bg);
  }
  .business-card {
    position: relative;
    width: 1200px;
    height: 761px;
    background: var(--card-white);
    overflow: hidden;
    font-family: "Alegreya", Georgia, serif;
    font-style: italic;
    font-weight: 400;
  }
  .card-wave {
    position: absolute;
    inset: 0;
    width: 1200px;
    height: 761px;
  }
  .wave-shadow { fill: var(--curve-shadow); }
  .wave-green { fill: var(--leaf-green); }
  .scripture {
    position: absolute;
    left: 80px;
    top: 86px;
    margin: 0;
    color: var(--card-white);
    font-size: 44px;
    line-height: 86px;
    letter-spacing: 0.5px;
    white-space: nowrap;
  }
  .scripture span { display: block; }
  .org-mark {
    position: absolute;
    left: 585px;
    top: 360px;
    display: flex;
    align-items: center;
    gap: 40px;
    color: var(--ink);
  }
  .org-mark-circle {
    width: 190px;
    height: 190px;
    border: 5px solid var(--ink);
    border-radius: 50%;
    box-sizing: border-box;
    flex: none;
  }
  .org-name {
    margin: 0;
    font-size: 54px;
    line-height: 64px;
    white-space: nowrap;
  }
  .org-name span { display: block; }
</style>
</head>
<body>
  <main class="business-card">
    <svg class="card-wave" viewBox="0 0 1200 761" aria-hidden="true">
      <path class="wave-shadow" d="M0,0 H1200 V40 C1160,262 940,318 676,350 C380,388 170,520 80,761 H0 Z"/>
      <path class="wave-green" d="M0,0 H1200 V28 C1150,245 920,300 650,332 C360,368 150,500 52,761 H0 Z"/>
    </svg>

    <p class="scripture">
      <span>“I was hungry and you gave me something to eat;</span>
      <span>"I was thirsty and you gave me something to drink;</span>
      <span>"I was a stranger and you invited me in."</span>
    </p>

    <div class="org-mark">
      <div class="org-mark-circle"></div>
      <p class="org-name">
        <span>Alder Ridge</span>
        <span>Helping Harbor</span>
      </p>
    </div>
  </main>
</body>
</html>
```